Kinward Harbor Center
Stationary and Business Cards
Kinward Harbor Center -
Creative Brief
Bright & Fun-filled
Marisol Thackery
48 Alder Lane Morristown, NJ 07931
marisol.thackery@alderlanehub.org
www.alderlanehub.org

```html
<!DOCTYPE html>
<html lang="en">
<head>
<meta charset="utf-8">
<title>Kinward Harbor Center – Stationery</title>
<link href="https://fonts.googleapis.com/css2?family=Open+Sans:wght@400;600&display=swap" rel="stylesheet">
<style>
:root{
  --backdrop:#9c9ea0;
  --paper:#ffffff;
  --navy:#0f2a5c;
  --blue:#2b6cc4;
  --blue-light:#5d97dd;
  --orange:#e2862f;
  --ink:#3a3f47;
  --grey:#b9bcc2;
}
*{margin:0;padding:0;box-sizing:border-box}
html,body{width:1200px;height:626px;overflow:hidden}
body{background:var(--backdrop);position:relative;font-family:"Open Sans",Arial,sans-serif;color:var(--ink)}
.sheet{position:absolute;background:var(--paper);overflow:hidden;box-shadow:0 1px 3px rgba(0,0,0,.25)}
.business-card{left:34px;top:307px;width:163px;height:125px}
.letterhead{left:233px;top:34px;width:427px;height:561px}
.envelope-back{left:682px;top:72px;width:489px;height:228px}
.envelope-front{left:682px;top:336px;width:489px;height:254px}

.brand{position:absolute;display:flex;flex-direction:column;align-items:center;text-align:center}
.brand-mark{width:14px;height:14px;border-radius:50%;background:var(--blue);margin-bottom:3px}
.brand-name{font-weight:600;color:var(--navy);letter-spacing:.08em;text-transform:uppercase;white-space:nowrap}
.brand-tagline{color:var(--ink);white-space:nowrap;margin-top:1px;opacity:.8}

.contact{position:absolute;text-align:right;line-height:1.45;color:var(--ink);white-space:nowrap}
.website{position:absolute;color:var(--orange);white-space:nowrap}
.holder-name{position:absolute;font-weight:600;color:var(--navy);white-space:nowrap}
.swoosh{position:absolute;left:0;bottom:0;width:100%}
</style>
</head>
<body>

<svg width="0" height="0" style="position:absolute">
  <defs>
    <linearGradient id="band" x1="0" x2="1" y1="0" y2="0">
      <stop offset="0" stop-color="#0f2a5c"/>
      <stop offset=".55" stop-color="#2b6cc4"/>
      <stop offset="1" stop-color="#163a78"/>
    </linearGradient>
    <linearGradient id="flap" x1="0" x2="1" y1="0" y2="0">
      <stop offset="0" stop-color="#0d2452"/>
      <stop offset=".5" stop-color="#4a8ad8"/>
      <stop offset="1" stop-color="#0d2452"/>
    </linearGradient>
    <symbol id="swoosh-shape" viewBox="0 0 400 60" preserveAspectRatio="none">
      <path d="M0 18 Q190 4 400 26 L400 60 L0 60 Z" fill="#c7cad0"/>
      <path d="M0 20 Q200 2 400 20" fill="none" stroke="#e2862f" stroke-width="1"/>
      <path d="M0 32 Q210 8 400 34 L400 60 L0 60 Z" fill="url(#band)"/>
      <path d="M0 30 Q210 6 400 32" fill="none" stroke="#ffffff" stroke-width="2"/>
    </symbol>
  </defs>
</svg>

<!-- Business card -->
<div class="sheet business-card">
  <div class="brand" style="left:8px;top:26px">
    <span class="brand-mark"></span>
    <span class="brand-name" style="font-size:5px">Kinward Harbor Center</span>
    <span class="brand-tagline" style="font-size:3px">Building Strong Families Together</span>
  </div>
  <div class="contact" style="right:8px;top:10px;font-size:3.4px">
    P: 973-555-0142<br>F: 973-555-0143<br>marisol.thackery@alderlanehub.org<br>48 Alder Lane Morristown, NJ 07931<br>www.alderlanehub.org
  </div>
  <div class="holder-name" style="right:10px;top:78px;font-size:5px">Marisol Thackery</div>
  <svg class="swoosh" height="34"><use href="#swoosh-shape" width="100%" height="100%"/></svg>
</div>

<!-- Letterhead -->
<div class="sheet letterhead">
  <div class="brand" style="left:26px;top:24px">
    <span class="brand-mark" style="width:18px;height:18px"></span>
    <span class="brand-name" style="font-size:6.5px">Kinward Harbor Center</span>
    <span class="brand-tagline" style="font-size:4px">Building Strong Families Together</span>
  </div>
  <div class="contact" style="right:22px;top:22px;font-size:4.8px">
    P: 973-555-0142<br>F: 973-555-0143<br>marisol.thackery@alderlanehub.org<br>48 Alder Lane Morristown, NJ 07931
  </div>
  <div class="website" style="right:22px;bottom:60px;font-size:5px">www.alderlanehub.org</div>
  <svg class="swoosh" height="62"><use href="#swoosh-shape" width="100%" height="100%"/></svg>
</div>

<!-- Envelope back -->
<div class="sheet envelope-back">
  <svg width="489" height="228" viewBox="0 0 489 228" style="position:absolute;left:0;top:0">
    <path d="M0 0 H489 V112 Q244 90 0 112 Z" fill="url(#flap)"/>
    <path d="M0 112 Q244 90 489 112" fill="none" stroke="#c7cad0" stroke-width="2"/>
  </svg>
</div>

<!-- Envelope front -->
<div class="sheet envelope-front">
  <div class="brand" style="left:20px;top:40px">
    <span class="brand-mark" style="width:16px;height:16px"></span>
    <span class="brand-name" style="font-size:6px">Kinward Harbor Center</span>
    <span class="brand-tagline" style="font-size:3.8px">Building Strong Families Together</span>
  </div>
  <div class="contact" style="right:60px;top:40px;font-size:4.6px;text-align:left">
    P: 973-555-0142<br>F: 973-555-0143<br>marisol.thackery@alderlanehub.org<br>48 Alder Lane Morristown, NJ 07931
  </div>
  <div class="website" style="right:16px;bottom:58px;font-size:5px">www.alderlanehub.org</div>
  <svg class="swoosh" height="60"><use href="#swoosh-shape" width="100%" height="100%"/></svg>
</div>

</body>
</html>
```